Business card design for crowd sourced review site.

I need a business card magnet design for an online, crowd-sourced, restaurant review site strictly for Kosher restaurants.
It is similar to RoamLedger but catering to a very particular crowd.
The markets it will be distributed in are flooded with business card fridge magnets so this needs to be eye-catching and unique. The Business name is PlateMarks
The website isnt finished but you can see the basic setup here
http://restaurant.vintrello.com/

The second image i included is another logo design I liked and was thinking about using and decided I will probably also make a SECOND custom cut business card in the shape of that icon. Bonus if you can throw that in also.

Target Market(s)

Jewish consumers aged 20-35

Industry/Entity Type

Business

Contact Information for Business Card

see description.
Design should not be too crowded and should in eye-catching. Will mainly be used as fridge magnets.

Requirements
Must have
• Website address. logo.
Nice to have
• tagline. (Honest reviews of kosher restaurants, written by kosher diners)
• Im not a professional but I personally think the color blue goes along with this concept. ill leave it to you to decide.
Should not have
• any religious symbols.

```html
<!DOCTYPE html>
<html lang="en">
<head>
<meta charset="utf-8">
<title>PlateMarks – Business Card</title>
<link rel="stylesheet" href="https://fonts.googleapis.com/css2?family=PT+Sans:wght@400;700&display=swap">
<style>
  :root {
    --page-bg: #e9e6e1;
    --card-black: #0b0b0b;
    --card-charcoal: #2a2a2a;
    --red-deep: #7a0b0b;
    --red-main: #c4161c;
    --red-bright: #e0262a;
    --silver-light: #f3f1ef;
    --silver-dark: #9c9693;
    --text-light: #ffffff;
    --text-soft: #f2dede;
    --tagline: #e6e0dc;
  }
  * { box-sizing: border-box; margin: 0; padding: 0; }
  html, body {
    width: 1200px; height: 969px; overflow: hidden;
    background: var(--page-bg);
    font-family: "PT Sans", "Verdana", sans-serif;
  }
  .card {
    position: absolute; left: 75px; top: 185px;
    width: 1050px; height: 600px;
    overflow: hidden;
    box-shadow: 0 18px 40px rgba(0,0,0,0.25);
  }
  .card-art { position: absolute; inset: 0; width: 100%; height: 100%; }
  .brand {
    position: absolute; left: 62px; top: 168px;
    display: flex; align-items: center; gap: 18px;
  }
  .brand-dot {
    width: 44px; height: 44px; border-radius: 50%;
    background: var(--red-bright);
  }
  .brand-name {
    color: var(--text-light);
    font-size: 64px; font-weight: 400; letter-spacing: 1px;
    line-height: 1;
  }
  .contact {
    position: absolute; right: 24px; top: 160px;
    text-align: right; color: var(--text-light);
  }
  .person-name { font-size: 34px; font-weight: 700; line-height: 40px; }
  .person-role { font-size: 29px; line-height: 40px; color: var(--text-soft); }
  .address { margin-top: 22px; font-size: 26px; line-height: 36px; color: var(--text-soft); }
  .lines { margin-top: 18px; list-style: none; }
  .lines li {
    display: flex; justify-content: flex-end; align-items: center; gap: 12px;
    font-size: 26px; line-height: 40px; color: var(--text-soft);
  }
  .lines svg { width: 26px; height: 26px; fill: var(--text-light); flex: none; }
  .tagline {
    position: absolute; right: 24px; bottom: 14px;
    font-size: 23px; font-weight: 700; color: var(--tagline);
    letter-spacing: 0.2px; white-space: nowrap;
  }
</style>
</head>
<body>
<div class="card">
  <svg class="card-art" viewBox="0 0 1050 600" preserveAspectRatio="none" aria-hidden="true">
    <defs>
      <radialGradient id="blackField" cx="0.3" cy="0.35" r="0.8">
        <stop offset="0" stop-color="var(--card-charcoal)"/>
        <stop offset="1" stop-color="var(--card-black)"/>
      </radialGradient>
      <linearGradient id="redField" x1="0" y1="0" x2="0.4" y2="1">
        <stop offset="0" stop-color="var(--red-bright)"/>
        <stop offset="0.55" stop-color="var(--red-main)"/>
        <stop offset="1" stop-color="var(--red-deep)"/>
      </linearGradient>
      <linearGradient id="silverBand" x1="0" y1="0" x2="1" y2="0">
        <stop offset="0" stop-color="var(--silver-dark)"/>
        <stop offset="0.35" stop-color="var(--silver-light)"/>
        <stop offset="0.7" stop-color="var(--silver-dark)"/>
        <stop offset="1" stop-color="var(--silver-light)"/>
      </linearGradient>
    </defs>
    <rect width="1050" height="600" fill="url(#blackField)"/>
    <path d="M0 416 C120 470 220 520 330 470 C450 410 520 310 640 240 C770 165 900 120 1050 100 L1050 600 L0 600 Z" fill="url(#redField)"/>
    <path d="M0 416 C120 470 220 520 330 470 C450 410 520 310 640 240 C770 165 900 120 1050 100"
          fill="none" stroke="url(#silverBand)" stroke-width="18"/>
    <path d="M0 400 C120 452 220 502 325 454 C445 396 515 296 635 226 C765 151 900 106 1050 86"
          fill="none" stroke="#000" stroke-opacity="0.55" stroke-width="4"/>
  </svg>

  <div class="brand">
    <span class="brand-dot"></span>
    <span class="brand-name">PlateMarks</span>
  </div>

  <div class="contact">
    <p class="person-name">Daniel Mirov</p>
    <p class="person-role">President</p>
    <p class="address">4127 Larchmont Avenue<br>Cedar Glen, NY 11020</p>
    <ul class="lines">
      <li>555 0142 7781
        <svg viewBox="0 0 24 24"><path d="M3 9c0-3 4-5 9-5s9 2 9 5v2h-5V9c-1-.6-2.5-1-4-1s-3 .4-4 1v2H3zM6 13h12l2 7H4z"/></svg></li>
      <li>555 0198 3364
        <svg viewBox="0 0 24 24"><path d="M7 1h10a1 1 0 0 1 1 1v20a1 1 0 0 1-1 1H7a1 1 0 0 1-1-1V2a1 1 0 0 1 1-1zm1 3v14h8V4zm4 15.5a1.3 1.3 0 1 0 0 2.6 1.3 1.3 0 0 0 0-2.6z"/></svg></li>
      <li>555 0176 2209
        <svg viewBox="0 0 24 24"><path d="M6 2h10l2 2v5H6zM3 10h18a1 1 0 0 1 1 1v7h-4v4H6v-4H2v-7a1 1 0 0 1 1-1zm5 6v4h8v-4z"/></svg></li>
      <li>daniel@platemarks.com
        <svg viewBox="0 0 24 24"><path d="M2 5h20v14H2zm2 2v.5l8 5.5 8-5.5V7l-8 5z"/></svg></li>
      <li>www.platemarks.com
        <svg viewBox="0 0 24 24"><circle cx="12" cy="12" r="10"/><path d="M12 2v20M2 12h20" stroke="#a8151a" stroke-width="1.6" fill="none"/></svg></li>
    </ul>
  </div>

  <p class="tagline">Honest reviews of kosher restaurants, written by kosher diners</p>
</div>
</body>
</html>
```